We need a full website with logo/graphics/woocommerce for hemp-based company

This site will be velmoraxi.com. It is a website featuring the fact we are the only manufacturer to produce CBDP and THCP. It should be great on mobile and desktop. We will pay for any extensions needed and while it should be a simple site:

About Us
About the Laboratory
About CBDP
About THCP
Shop
Contact Us

Only 4 products on the site.

It can be wordpress or joomla. Your choice. You must install the final website on our server. We agree to pay for monthly support that must be submitted in your quote.

He have a great graphics designer that will assist keeping colors and graphics clean according to your specifications.

Industry/Entity Type

Hemp CBD THC

Coding

Coded - Design and coding required

Number of Pages Required

5+ page

Requirements
Must have
• A simple clean layout

```html
<!DOCTYPE html>
<html lang="en">
<head>
<meta charset="utf-8">
<title>Velmoraxi – About CBDP</title>
<link rel="stylesheet" href="https://fonts.googleapis.com/css2?family=Roboto:wght@400;500;700&family=Source+Sans+3:wght@400;600;700&family=Ubuntu:wght@500;700&display=swap">
<style>
:root{
  --green:#0f9d5a;
  --green-dark:#0b8a4e;
  --ink:#333;
  --text:#444;
  --muted:#777;
  --strip:#f4f4f4;
  --footer:#222;
  --btn:#2b2b2b;
  --white:#fff;
  --line:#ddd;
}
*{box-sizing:border-box;margin:0;padding:0}
html,body{width:1124px;height:1200px;overflow:hidden;background:var(--white)}
body{font-family:"Source Sans 3",sans-serif;color:var(--text);position:relative}

.topbar{height:35px;border-bottom:1px solid var(--line);display:flex;align-items:center;justify-content:space-between;padding:0 18px;font:400 12px "Roboto",sans-serif;color:#555}
.topbar .info{display:flex;gap:16px;align-items:center}
.topbar .info span{display:flex;align-items:center;gap:6px}

.header{height:99px;display:flex;align-items:center;padding:0 18px;position:relative}
.brand{display:flex;align-items:center;gap:10px;width:280px}
.brand .mark{width:62px;height:62px;border-radius:50%;background:var(--green)}
.brand .name{font:700 28px "Ubuntu",sans-serif;color:var(--green);line-height:1}
.brand .tag{font:500 8px "Ubuntu",sans-serif;color:var(--ink);margin-top:4px;letter-spacing:.1px}
.nav{display:flex;gap:16px;font:700 15.5px "Source Sans 3",sans-serif;color:var(--ink);text-transform:uppercase;margin-left:-1px}
.nav .active{color:var(--green)}
.hotline{position:absolute;left:888px;top:37px;display:flex;align-items:center;gap:14px}
.hotline .num{font:700 11px "Source Sans 3",sans-serif;color:var(--green);line-height:15px}
.hotline .mail{font:400 11px "Source Sans 3",sans-serif;color:var(--green)}

.catbar{height:49px;background:var(--green);display:flex;align-items:center;position:relative;color:var(--white)}
.catbar .cats{font:700 17px "Source Sans 3",sans-serif;margin-left:14px;width:170px}
.catbar .burger{width:14px;margin-left:0}
.search{position:absolute;left:236px;top:9px;width:543px;height:31px;display:flex;background:var(--white)}
.search .field{flex:1;font:400 13.5px "Roboto",sans-serif;color:#777;padding:7px 13px}
.search .select{width:145px;font:400 13.5px "Roboto",sans-serif;color:#666;padding:7px 0;display:flex;justify-content:space-between;padding-right:10px}
.search .go{width:53px;background:var(--btn);display:flex;align-items:center;justify-content:center}
.catbar .cart{position:absolute;left:1007px;top:15px;font:700 15px "Source Sans 3",sans-serif;display:flex;gap:8px;align-items:center}

.strip{height:83px;background:var(--strip);position:relative}
.prod{position:absolute;top:8px;display:flex;gap:14px}
.prod .thumb{width:73px;height:66px;background:linear-gradient(#fafafa,#ececec);display:flex;align-items:center;justify-content:center}
.prod .thumb i{display:block;width:14px;height:46px;border-radius:3px 3px 2px 2px;background:linear-gradient(#2a1a0e 0 26%,#b0741e 26%)}
.prod .title{font:700 11px "Roboto",sans-serif;color:var(--ink);margin-top:9px}
.prod .price{font:400 10px "Roboto",sans-serif;color:#888;margin-top:6px}
.prod .price.dark{font-weight:700;color:var(--ink)}

.content{padding:37px 47px 0}
.content h1{font:400 19.5px "Source Sans 3",sans-serif;color:var(--ink);margin:0 0 25px 3px}
.content p{font:400 16.6px/20.2px "Source Sans 3",sans-serif;color:var(--text);margin-bottom:20px;letter-spacing:-.1px}

.footer{position:absolute;left:0;top:830px;width:1124px;height:370px;background:var(--footer);color:var(--white);text-align:center}
.fnav{display:flex;justify-content:center;gap:25px;font:700 15px "Source Sans 3",sans-serif;margin-top:48px}
.fnote{width:760px;margin:44px auto 0;font:400 13.4px/23.5px "Roboto",sans-serif}
.social{display:flex;justify-content:center;gap:9px;margin-top:22px}
.social span{height:29px;min-width:29px;padding:0 7px;border:1px solid #888;border-radius:15px;font:600 9.5px/27px "Source Sans 3",sans-serif}
.copy{font:400 11px "Source Sans 3",sans-serif;margin-top:26px}
.pay{display:flex;justify-content:center;gap:8px;margin-top:17px}
.pay span{width:42px;height:28px;border-radius:2px;background:#eee;color:#333;font:700 8.5px/28px "Source Sans 3",sans-serif}
.totop{position:absolute;left:1061px;top:1140px;width:34px;height:34px;background:#f3f3f3;border:1px solid #999;display:flex;align-items:center;justify-content:center}
</style>
</head>
<body>

<div class="topbar">
  <span>Get 50% Off In Every Products - New Year 2021 Deals</span>
  <div class="info">
    <span><svg width="14" height="12" viewBox="0 0 14 12"><path d="M1 3l4-2 4 2 4-2v8l-4 2-4-2-4 2z" fill="#666"/></svg>Sydney, Australia</span>
    <span><svg width="15" height="12" viewBox="0 0 15 12"><path d="M1 2h8v7H1zM9 4h3l2 3v2H9z" fill="#666"/><circle cx="4" cy="10" r="1.6" fill="#666"/><circle cx="11.5" cy="10" r="1.6" fill="#666"/></svg>Free Delivery / Cash on Delivery</span>
  </div>
</div>

<header class="header">
  <div class="brand">
    <div class="mark"></div>
    <div>
      <div class="name">VELMORAXI</div>
      <div class="tag">THE ONLY PURVEYORS OF CBDP AND THCP</div>
    </div>
  </div>
  <nav class="nav">
    <span class="active">Home</span><span>About the Laboratory</span><span>About CBDP</span><span>About THCP</span><span>Shop</span><span>Contact</span>
  </nav>
  <div class="hotline">
    <svg width="40" height="42" viewBox="0 0 40 42" fill="none" stroke="#0f9d5a" stroke-width="3.5"><path d="M5 24v-6a15 15 0 0 1 30 0v6"/><rect x="3" y="20" width="7" height="12" rx="3" fill="#0f9d5a"/><rect x="30" y="20" width="7" height="12" rx="3" fill="#0f9d5a"/><path d="M33 32c0 5-5 7-12 7"/></svg>
    <div><div class="num">+1 555 014 2290</div><div class="mail">info@velmoraxi.com</div></div>
  </div>
</header>

<div class="catbar">
  <span class="cats">MAIN CATEGORIES</span>
  <svg class="burger" width="15" height="13" viewBox="0 0 15 13"><path d="M0 1h15M0 6.5h15M0 12h15" stroke="#fff" stroke-width="2"/></svg>
  <div class="search">
    <span class="field">Search products</span>
    <span class="select">All Categories<svg width="10" height="18" viewBox="0 0 10 18"><path d="M1 7l4 4 4-4" stroke="#333" stroke-width="1.6" fill="none"/></svg></span>
    <span class="go"><svg width="13" height="13" viewBox="0 0 13 13"><circle cx="5.5" cy="5.5" r="4" stroke="#fff" stroke-width="2" fill="none"/><path d="M8.5 8.5l3.5 3.5" stroke="#fff" stroke-width="2.2"/></svg></span>
  </div>
  <span class="cart">CART<svg width="21" height="18" viewBox="0 0 21 18" fill="none" stroke="#fff" stroke-width="1.4"><path d="M1 1h3l2 11h12l2-8H5"/><path d="M8 6v4M11 6v4M14 6v4M17 6v4"/><circle cx="8" cy="15.5" r="1.4"/><circle cx="16" cy="15.5" r="1.4"/></svg></span>
</div>

<div class="strip">
  <div class="prod" style="left:17px"><div class="thumb" role="img" aria-label="Tincture bottle product photo"><i></i></div><div><div class="title" style="margin-top:14px">Nova 12 Max</div><div class="price dark">$2,000.00</div></div></div>
  <div class="prod" style="left:227px"><div class="thumb" role="img" aria-label="Tincture bottle product photo"><i></i></div><div><div class="title">Loresm ipsum dolor sit</div><div class="price">$ 30.00</div></div></div>
  <div class="prod" style="left:455px"><div class="thumb" role="img" aria-label="Tincture bottle product photo"><i></i></div><div><div class="title">Loresm ipsum dolor sit</div><div class="price">$ 30.00</div></div></div>
  <div class="prod" style="left:667px"><div class="thumb" role="img" aria-label="Tincture bottle product photo"><i></i></div><div><div class="title">Loresm ipsum dolor sit</div><div class="price">$ 30.00</div></div></div>
  <div class="prod" style="left:881px"><div class="thumb" role="img" aria-label="Tincture bottle product photo"><i></i></div><div><div class="title">Loresm ipsum dolor sit</div><div class="price">$ 30.00</div></div></div>
</div>

<main class="content">
  <h1>ABOUT CBDP</h1>
  <p>We have posted an article about a new cannabinoid known as THCP. This new cannabinoid is believed to be more potent than THC. The Italian researchers who discovered THCP discovered a new cannabinoid as well similar to CBD called CBDP. The structure of THCP and CBDP are very similar to THC and CBD. CBDP has also a seven links molecular structure and researchers are studying this new cannabinoid to understand its effects and how it binds with our CB1 and CB2 receptors.</p>
  <p>This study added to new cannabinoids to a list of over 150 identified cannabinoids. As they have been recently discovered, we still don’t know that much about their medical properties.</p>
  <p>What is Cannabidiphorol?</p>
  <p>Mostly all-natural occurring cannabinoids have a five-link molecular structure. However, both THCP and CBDP have seven links molecular structure. This makes them unique cannabinoids. The Italian scientist that discovered both cannabinoids, believe this unique chemical structure have a lot of beneficial medical properties. Nonetheless, currently we don’t know that much about CBDP and its ability to bind with the CB1 and CB2 receptors.</p>
  <p>Cannabidiphorol has many potential uses. For instance, it is believed it has a key role in determining the specific entourage effect derived from a particular cannabis strain. Moreover, it might also be important in how a cannabis strain interacts with each individual. This would explain why individuals experience different effects with the same cannabis strain.</p>
  <p>Both THCP and CBDP have analgesic and relaxant properties. In addition, the same as CBD, CDBP has a great potential to be used as a treatment for neurological disorders such as epilepsy. As a matter of fact, CBD is already used in the treatment of epilepsy (Calmedrin is an FDA approved drug for the treatment of two rare forms of child epilepsy).</p>
</main>

<footer class="footer">
  <nav class="fnav"><span>SHOP</span><span>MY ACCOUNT</span><span>CART</span><span>ABOUT CBDP</span><span>ABOUT THCP</span><span>ABOUT OUR LABORATORY</span><span>CONTACT</span></nav>
  <p class="fnote">Commodo viverra maecenas accumsan lacus vel facilisis volutpat. Est velit egestas dui id ornare arcu. Erat nam at lectus urna duis. Libero nunc consequat interdum varius sit amet mattis. Nunc faucibus a pellentesque sit amet porttitor eget dolor. Amet consectetur adipiscing elit duis tristique. Mus mauris vitae ultricies leo integer. Vitae ultricies leo integer malesuada nunc vel. Venenatis cras sed felis eget velit aliquet sagittis id consectetur. Eget felis eget nunc lobortis mattis.</p>
  <div class="social"><span>Chirpa</span><span>Facio</span><span>Talko</span><span>Lumo</span><span>Ringo</span></div>
  <div class="copy">Copyright © Velmoraxi 2021, All Rights Reserved</div>
  <div class="pay"><span>Payvo</span><span>Bank</span><span>Vesta</span><span>Duocard</span><span>Findly</span><span>Amerigo</span><span>Tempo</span><span>Paylo</span></div>
</footer>

<div class="totop"><svg width="14" height="16" viewBox="0 0 14 16"><path d="M7 15V2M1 8l6-6 6 6" stroke="#333" stroke-width="2.2" fill="none"/></svg></div>

</body>
</html>
```